Invitation card to the opening of BRAVORA FITNESS CLUB

A successful training plan starts with BRAVORA Fitness!
Join us for our grand opening! OPEN HOUSE AND YOU ARE INVITED!
Tuesday 1st of August, 2017
Classes start from 7.30am till 9.30pm.
Explore the most fun, exciting, challenging and effective training system in the region.
Healthy drinks and delicious food will be provided.
We hope to see you there!

www.bravorafitnessclub.example
APP: BRAVORAFITQZN
Tel: 81-42 09 15

Industry/Entity Type

Fitness

Colors

Designer to choose colors to be used in the design.

Requirements
Must have
• Elegant card
Nice to have
• Logo in the background
Should not have
• pictures

```html
<!DOCTYPE html>
<html lang="en">
<head>
<meta charset="utf-8">
<title>Bravora Fitness Club – Grand Opening</title>
<link rel="stylesheet" href="https://fonts.googleapis.com/css2?family=Anton&family=Cinzel:wght@400&family=Josefin+Sans:wght@400;600&family=Montserrat:wght@500;700;800&display=swap">
<style>
  :root {
    --ink: #0b0b0b;
    --band: #2a2826;
    --gold: #d9b25c;
    --gold-soft: #c9a45a;
    --gold-deep: #9c7a36;
    --silver: #e6e6e6;
    --red: #c41313;
    --red-deep: #8e0b0b;
    --white: #f5f5f5;
    --grey: #6d6d6d;
  }
  * { margin: 0; padding: 0; box-sizing: border-box; }
  html, body { width: 950px; height: 1200px; overflow: hidden; background: var(--ink); }
  .invite {
    position: relative; width: 950px; height: 1200px; overflow: hidden;
    background: var(--ink); font-family: "Montserrat", sans-serif; color: var(--white);
  }
  .invite__backdrop {
    position: absolute; inset: 0;
    background:
      radial-gradient(ellipse 420px 300px at 170px 420px, #2b2b2b 0%, transparent 70%),
      radial-gradient(ellipse 300px 260px at 800px 250px, #262626 0%, transparent 70%),
      radial-gradient(ellipse 260px 220px at 820px 860px, #242424 0%, transparent 70%),
      linear-gradient(180deg, #141414 0%, #0d0d0d 55%, #121212 100%);
  }
  .tagline {
    position: absolute; top: 46px; left: 0; width: 100%; text-align: center;
    font-family: "Josefin Sans", sans-serif; color: var(--gold-soft);
    font-size: 27px; line-height: 38px; letter-spacing: 1px; text-transform: uppercase;
  }
  .brand { position: absolute; top: 148px; left: 0; width: 100%; text-align: center; }
  .brand__ring {
    width: 160px; height: 160px; margin: 0 auto 24px; border-radius: 50%;
    border: 9px solid #9a9a9a;
  }
  .brand__name {
    font-family: "Cinzel", serif; font-weight: 400; color: var(--white);
    font-size: 92px; line-height: 92px; letter-spacing: 2px;
  }
  .brand__sub {
    font-family: "Cinzel", serif; font-weight: 400; color: var(--white);
    font-size: 34px; letter-spacing: 16px; margin-top: 14px; padding-left: 16px;
  }
  .date-band {
    position: absolute; left: 330px; top: 540px; width: 700px; height: 170px;
    background: linear-gradient(90deg, #1d1c1b, var(--band) 40%, #1a1918);
    transform: rotate(-6deg); transform-origin: left top;
    box-shadow: 0 6px 18px rgba(0,0,0,.6);
  }
  .athlete-photo {
    position: absolute; left: 345px; top: 500px; width: 160px; height: 260px;
    background: radial-gradient(ellipse at 40% 45%, var(--red) 0%, var(--red-deep) 100%);
  }
  .headline {
    position: absolute; left: 58px; top: 508px; width: 290px;
    transform: rotate(-5deg); transform-origin: left top;
  }
  .headline__lead { font-family: "Josefin Sans", sans-serif; font-size: 22px; letter-spacing: 1px; text-transform: uppercase; }
  .headline__grand {
    font-family: "Anton", sans-serif; font-weight: 400; font-size: 108px; line-height: 106px; color: var(--gold);
    text-shadow: 0 3px 0 var(--gold-deep);
  }
  .headline__opening {
    font-family: "Anton", sans-serif; font-size: 64px; line-height: 68px; color: var(--silver);
    text-shadow: 0 3px 0 #7e7e7e;
  }
  .headline__open-house { font-family: "Josefin Sans", sans-serif; font-size: 24px; color: var(--red); text-transform: uppercase; margin-top: 2px; }
  .headline__invite { display: flex; align-items: flex-end; gap: 8px; margin-top: 2px; }
  .headline__you-are { font-family: "Josefin Sans", sans-serif; font-size: 23px; line-height: 22px; text-transform: uppercase; }
  .headline__invited {
    font-family: "Anton", sans-serif; font-size: 42px; line-height: 46px; color: var(--white);
    background: var(--red); padding: 0 8px;
  }
  .schedule {
    position: absolute; left: 525px; top: 568px; width: 320px;
    transform: rotate(-6deg); transform-origin: left top;
  }
  .schedule__day { font-family: "Josefin Sans", sans-serif; font-size: 36px; letter-spacing: 12px; }
  .schedule__date { font-weight: 800; font-size: 44px; line-height: 48px; color: var(--gold); }
  .schedule__from { font-family: "Josefin Sans", sans-serif; font-size: 20px; letter-spacing: 1.5px; text-transform: uppercase; margin-top: 4px; }
  .schedule__hours { font-weight: 800; font-size: 30px; color: var(--red); }
  .schedule__year {
    position: absolute; left: 318px; top: 110px; font-weight: 800;
    font-size: 46px; color: var(--grey); transform: rotate(-90deg); transform-origin: left top;
  }
  .pitch {
    position: absolute; left: 150px; top: 790px; width: 640px; text-align: center;
    transform: rotate(-6deg);
  }
  .pitch__lead, .pitch__tail { font-family: "Josefin Sans", sans-serif; font-size: 22px; letter-spacing: 1px; text-transform: uppercase; }
  .pitch__main { font-weight: 800; font-size: 31px; line-height: 36px; color: var(--red); text-transform: uppercase; }
  .perks {
    position: absolute; left: 170px; top: 905px; width: 600px; padding: 10px 0; text-align: center;
    background: linear-gradient(90deg, transparent, #2b2927 20%, #2b2927 80%, transparent);
    transform: rotate(-6deg);
    font-weight: 800; font-size: 21px; line-height: 29px; letter-spacing: 1px; color: var(--gold-soft); text-transform: uppercase;
  }
  .footer-band {
    position: absolute; left: -30px; top: 1075px; width: 1020px; height: 110px;
    background: linear-gradient(90deg, #1f1e1d, var(--band) 50%, #1f1e1d);
    transform: rotate(-6deg);
  }
  .farewell { position: absolute; left: 62px; top: 1068px; transform: rotate(-6deg); transform-origin: left top; }
  .farewell__soft { font-size: 32px; font-weight: 500; }
  .farewell__bold { font-size: 32px; font-weight: 800; color: var(--red); text-transform: uppercase; line-height: 36px; }
  .contact {
    position: absolute; left: 440px; top: 1050px; transform: rotate(-6deg); transform-origin: left top;
    border-left: 2px solid var(--red-deep); padding-left: 22px;
  }
  .contact__web { font-weight: 700; font-size: 21px; display: flex; align-items: center; gap: 8px; white-space: nowrap; }
  .contact__row { display: flex; align-items: center; gap: 10px; margin-top: 6px; font-weight: 700; white-space: nowrap; }
  .contact__app { color: var(--red); font-size: 18px; }
  .contact__tel { color: var(--red); font-size: 23px; }
  .dot { width: 14px; height: 14px; border-radius: 50%; background: var(--red); display: inline-block; flex: none; }
  .dot--white { background: var(--white); }
</style>
</head>
<body>
<main class="invite">
  <div class="invite__backdrop" role="img" aria-label="Dark smoky photographic backdrop of athletes training in a gym"></div>

  <p class="tagline">A successful<br>training plan starts with</p>

  <header class="brand">
    <div class="brand__ring"></div>
    <div class="brand__name">BRAVORA</div>
    <div class="brand__sub">FITNESS</div>
  </header>

  <div class="date-band"></div>
  <div class="athlete-photo" role="img" aria-label="Red-toned photo of an athlete flexing"></div>

  <section class="headline">
    <p class="headline__lead">Join us for our</p>
    <h1 class="headline__grand">GRAND</h1>
    <p class="headline__opening">OPENING!</p>
    <p class="headline__open-house">Open house and</p>
    <div class="headline__invite">
      <span class="headline__you-are">You<br>are</span>
      <span class="headline__invited">INVITED!</span>
    </div>
  </section>

  <section class="schedule">
    <p class="schedule__day">TUESDAY</p>
    <p class="schedule__date">1ST AUGUST</p>
    <p class="schedule__from">Classes start from</p>
    <p class="schedule__hours">7:30 AM - 9:30PM</p>
    <span class="schedule__year">2017</span>
  </section>

  <section class="pitch">
    <p class="pitch__lead">Explore the most</p>
    <p class="pitch__main">Fun, exciting, challenging and<br>effective training system</p>
    <p class="pitch__tail">In the region</p>
  </section>

  <p class="perks">Healthy drinks and<br>delicious food will be provided.</p>

  <div class="footer-band"></div>
  <section class="farewell">
    <p class="farewell__soft">We hope to</p>
    <p class="farewell__bold">See you there!</p>
  </section>

  <section class="contact">
    <p class="contact__web"><span class="dot"></span>www.bravorafitnessclub.example</p>
    <div class="contact__row">
      <span class="dot dot--white"></span><span class="contact__app">BRAVORAFITQZN</span>
      <svg width="20" height="20" viewBox="0 0 24 24" aria-hidden="true"><circle cx="12" cy="12" r="11" fill="#f5f5f5"/><path d="M8 6.5c.6-.4 1.3-.3 1.6.3l1 2c.3.5.1 1-.3 1.4l-.7.6c.6 1.4 1.8 2.6 3.2 3.2l.6-.7c.4-.4 1-.5 1.4-.3l2 1c.6.3.7 1 .3 1.6-.8 1.2-2.2 1.6-3.5 1.1-3-1.1-5.4-3.5-6.5-6.5-.5-1.300-.1-2.7 1.1-3.5z" fill="#1c1b1b"/></svg>
      <span class="contact__tel">81-42 09 15</span>
    </div>
  </section>
</main>
</body>
</html>
```